General contractor/GM consaltant business card

I need a card for my contracting company in North Dakota, we build industrial buildings for the oil feild and oil feild related companies offices, shops, airplain hangars, airports ext. We have a familly atmosphere on the job and are very relational and personal.
Industry/Entity Type
Industrial
Contact Information for Business Card
Hollowpine Crafters LLC.
Dale T.Voskuijl
4873 Quenwick dr. Colorado Springs, CO. 80462
Cell# 406-738-1452
dale@hollowpinecrafters.example

```html
<!DOCTYPE html>
<html lang="en">
<head>
<meta charset="utf-8">
<title>Hollowpine Crafters LLC. — Business Card</title>
<link rel="stylesheet" href="https://fonts.googleapis.com/css2?family=Montserrat:wght@500;600&display=swap">
<style>
  :root {
    --backdrop: #9a9a9a;
    --card: #ffffff;
    --navy: #0b3a60;
    --green: #6aa63c;
    --shadow: rgba(0, 0, 0, 0.55);
  }
  * { margin: 0; padding: 0; box-sizing: border-box; }
  html, body {
    width: 1200px;
    height: 1000px;
    overflow: hidden;
    background: var(--backdrop);
    font-family: "Montserrat", sans-serif;
  }
  .canvas { position: relative; width: 1200px; height: 1000px; }
  .card {
    position: absolute;
    top: 375px;
    height: 252px;
    background: var(--card);
    box-shadow: 5px 5px 6px var(--shadow);
    overflow: hidden;
  }
  .card--front { left: 111px; width: 444px; }
  .card--back { left: 628px; width: 437px; }

  .brand-name {
    position: absolute;
    color: var(--navy);
    font-weight: 600;
    text-align: center;
    line-height: 1.1;
  }
  .card--front .brand-name {
    left: 0; right: 0; top: 100px;
    font-size: 32px;
  }
  .card--back .brand-name {
    left: 240px; width: 196px; top: 22px;
    font-size: 21px;
  }

  .accent-wave { position: absolute; left: 0; top: 0; }

  .person { position: absolute; left: 34px; top: 66px; color: var(--navy); }
  .person__name { font-size: 17px; font-weight: 500; letter-spacing: 0.2px; }
  .person__role { font-size: 12px; font-weight: 500; margin: 3px 0 0 44px; }

  .contact { position: absolute; color: var(--navy); font-weight: 500; }
  .contact--address { left: 199px; top: 115px; font-size: 13px; line-height: 18px; }
  .contact--phone { left: 234px; top: 167px; font-size: 11px; }
  .contact--email { left: 232px; top: 207px; font-size: 11.5px; }
  .contact-icon { position: absolute; }
  .contact-icon--phone { left: 192px; top: 158px; }
  .contact-icon--email { left: 192px; top: 203px; }
</style>
</head>
<body>
<div class="canvas">
  <section class="card card--front">
    <div class="brand-name">Hollowpine<br>Crafters LLC.</div>
  </section>

  <section class="card card--back">
    <svg class="accent-wave" width="437" height="252" viewBox="0 0 437 252" aria-hidden="true">
      <path d="M0 0 L16 0 C26 22 23 70 26 110 C34 200 150 248 292 252 L0 252 Z" fill="var(--navy)"/>
    </svg>

    <div class="brand-name">Hollowpine<br>Crafters LLC.</div>

    <div class="person">
      <div class="person__name">Dale T.Voskuijl</div>
      <div class="person__role">Founder</div>
    </div>

    <div class="contact contact--address">4873 Quenwick dr. Colorado<br>Springs, CO. 80462</div>

    <svg class="contact-icon contact-icon--phone" width="34" height="34" viewBox="0 0 24 24" aria-hidden="true">
      <path fill="var(--green)" d="M6.6 10.8c1.4 2.8 3.8 5.1 6.6 6.6l2.2-2.2c.3-.3.7-.4 1-.2 1.1.4 2.3.6 3.6.6.6 0 1 .4 1 1V20c0 .6-.4 1-1 1C10.6 21 3 13.4 3 4c0-.6.4-1 1-1h3.5c.6 0 1 .4 1 1 0 1.3.2 2.5.6 3.6.1.3 0 .7-.2 1l-2.3 2.2z"/>
    </svg>
    <div class="contact contact--phone"># 406-738-1452</div>

    <svg class="contact-icon contact-icon--email" width="33" height="24" viewBox="0 0 33 24" aria-hidden="true">
      <rect x="1.5" y="1.5" width="30" height="21" fill="none" stroke="var(--green)" stroke-width="3"/>
      <path d="M3 3 L16.5 13 L30 3" fill="none" stroke="var(--green)" stroke-width="3"/>
    </svg>
    <div class="contact contact--email">dale@hollowpinecrafters.example</div>
  </section>
</div>
</body>
</html>
```